Corvane Large Loss Tradeshow Booth Design

We need a tradeshow booth design for a 10x20 booth. We are a COMMERCIAL ONLY disaster restoration company focusing on water and flood restoration, fire and smoke remediation, mold and biohazard, structural repair and asset protection.

These are the links to the booth we need graphics designed for. The spec sheets for them are also in the attachments.
https://www.expostallden.com/Pelmora-Radial-Swift-Truss-p/pelmora.htm?CartID=2
https://www.expostallden.com/Tidecrest-39-Counter-p/tdc-39.htm?CartID=1
https://www.expostallden.com/6ft-Stretch-Table-Cover-p/tbl-6-stretch.htm?CartID=5

Target Market(s)

Real Estate, Educational Facilities, Hospitality Facilities, Medical Facilities

Industry/Entity Type

Construction

Requirements
Must have
• Our logo. The colors from the attached presentation. Pictures of COMMERCIAL ONLY facilities and losses (can use some from attached presentation). Our services (water and flood, fire and smoke, mold and biohazard, structural repair, asset protection). Our slogan (Exceeding your expectations when you need it most).
Nice to have
• Include the above
Should not have
• Do not include anything residential looking at all (no pictures). Do not include the case studies on the pictures.

```html
<!DOCTYPE html>
<html lang="en">
<head>
<meta charset="utf-8">
<title>Corvane Large Loss – Tradeshow Booth Graphics</title>
<link href="https://fonts.googleapis.com/css2?family=Titillium+Web:wght@700;900&display=swap" rel="stylesheet">
<style>
  :root {
    --wall-light: #d4d5d7;
    --wall-dark: #6b6c70;
    --board: #ffffff;
    --sky-deep: #1f6fbf;
    --sky-mid: #3e94dc;
    --sky-light: #8fd0f5;
    --stripe: #1a5ea8;
    --orange: #f28c1e;
    --orange-ink: #6a3a08;
    --service-grey: #6d6e70;
    --mist: #e9eaeb;
    --water-dark: #3b3b3b;
  }
  * { box-sizing: border-box; margin: 0; padding: 0; }
  html, body { width: 1200px; height: 502px; overflow: hidden; }
  body {
    position: relative;
    font-family: "Titillium Web", "Arial Narrow", sans-serif;
    background: linear-gradient(to bottom, var(--wall-light) 0 364px, var(--wall-dark) 364px 100%);
  }
  .board {
    position: absolute; left: 19px; top: 54px; width: 1162px; height: 392px;
    background: var(--board);
    box-shadow: 6px 7px 10px rgba(0,0,0,0.35);
  }
  .panel {
    position: absolute; top: 86px; height: 344px; overflow: hidden;
  }
  .panel__photo {
    position: absolute; inset: 0;
    background: linear-gradient(to bottom,
      #f4f5f6 0%, #dcdddf 30%, var(--mist) 55%, #bdbdbd 72%, #5c5c5c 82%, var(--water-dark) 100%);
  }
  .panel__sky, .panel__base {
    position: absolute; left: 0; width: 100%; display: block;
  }
  .panel__sky { top: 0; height: 100px; }
  .panel__base { bottom: 0; height: 30px; }
  .panel__content {
    position: absolute; left: 0; right: 0; text-align: center;
  }
  .brand__name {
    color: var(--orange); font-weight: 700; line-height: 1;
    letter-spacing: 0.5px;
  }
  .brand__name span { display: block; }
  .brand__primary { font-size: 30px; }
  .brand__secondary { font-size: 10px; margin-top: 3px; }
  .services { list-style: none; color: var(--service-grey); font-weight: 700; text-transform: uppercase; }
  .services--wide { font-size: 12.5px; line-height: 13.6px; margin-top: 14px; }
  .services--narrow { font-size: 7.6px; line-height: 9.2px; }
  .slogan {
    color: var(--orange); font-weight: 900; text-transform: uppercase;
    font-size: 13px; line-height: 16px; margin-top: 14px;
    text-shadow: -1px 0 var(--orange-ink), 1px 0 var(--orange-ink), 0 -1px var(--orange-ink), 0 1px var(--orange-ink);
  }
</style>
</head>
<body>
<div class="board"></div>

<svg width="0" height="0" style="position:absolute">
  <defs>
    <linearGradient id="sky" x1="0" y1="0" x2="0" y2="1">
      <stop offset="0" stop-color="#2b7fd0"/>
      <stop offset="0.6" stop-color="#5aaee8"/>
      <stop offset="1" stop-color="#9ad6f6"/>
    </linearGradient>
  </defs>
</svg>

<!-- Services panel, left -->
<section class="panel" style="left:52px;width:154px">
  <div class="panel__photo" role="img" aria-label="Flooded commercial downtown street with office towers in mist"></div>
  <svg class="panel__sky" viewBox="0 0 100 100" preserveAspectRatio="none">
    <path d="M0 0H100V86C65 80 30 66 0 60Z" fill="url(#sky)"/>
    <path d="M0 60C30 66 65 80 100 86V92C65 84 30 70 0 64Z" fill="#a9dcf7" opacity="0.7"/>
  </svg>
  <svg class="panel__base" viewBox="0 0 100 30" preserveAspectRatio="none">
    <path d="M0 30V12C35 4 70 2 100 0V30Z" fill="var(--orange)"/>
  </svg>
  <div class="panel__content" style="top:100px">
    <div class="brand__name"><span class="brand__primary" style="font-size:26px">CORVANE</span><span class="brand__secondary">RESTORATION SERVICES</span></div>
    <ul class="services services--wide">
      <li>Water and Flood</li><li>Fire and Smoke</li><li>Mold and Biohazard</li><li>Structural Repair</li><li>Asset Protection</li>
    </ul>
  </div>
</section>

<!-- Narrow services panel -->
<section class="panel" style="left:224px;width:103px">
  <div class="panel__photo" role="img" aria-label="Office towers reflected in floodwater"></div>
  <svg class="panel__sky" viewBox="0 0 100 100" preserveAspectRatio="none">
    <path d="M0 0H100V78C65 76 30 80 0 82Z" fill="url(#sky)"/>
    <path d="M0 82C30 80 65 76 100 78V82C65 80 30 84 0 86Z" fill="var(--stripe)"/>
  </svg>
  <svg class="panel__base" viewBox="0 0 100 30" preserveAspectRatio="none">
    <path d="M0 30V4C40 4 70 6 100 4V30Z" fill="var(--orange)"/>
  </svg>
  <div class="panel__content" style="top:157px">
    <ul class="services services--narrow">
      <li>Water and Flood</li><li>Fire and Smoke</li><li>Mold and Biohazard</li><li>Structural Repair</li><li>Asset Protection</li>
    </ul>
  </div>
</section>

<!-- Slogan panel -->
<section class="panel" style="left:356px;width:150px">
  <div class="panel__photo" role="img" aria-label="Flooded commercial plaza with trees and office buildings"></div>
  <svg class="panel__sky" viewBox="0 0 100 100" preserveAspectRatio="none">
    <path d="M0 0H100V50L0 70Z" fill="url(#sky)"/>
    <path d="M0 70L100 50V53L0 73Z" fill="var(--stripe)"/>
  </svg>
  <svg class="panel__base" viewBox="0 0 100 30" preserveAspectRatio="none">
    <path d="M0 30V8C40 2 70 0 100 0V30Z" fill="var(--orange)"/>
  </svg>
  <div class="panel__content" style="top:96px">
    <div class="brand__name"><span class="brand__primary" style="font-size:28px">CORVANE</span><span class="brand__secondary">RESTORATION SERVICES</span></div>
    <p class="slogan">Exceeding your<br>expectations when<br>you need it most</p>
  </div>
</section>

<!-- Center narrow services panel -->
<section class="panel" style="left:558px;width:103px">
  <div class="panel__photo" role="img" aria-label="Flooded plaza between office towers"></div>
  <svg class="panel__sky" viewBox="0 0 100 100" preserveAspectRatio="none">
    <path d="M0 0H100V40C65 44 30 52 0 58Z" fill="url(#sky)"/>
    <path d="M0 58C30 52 65 44 100 40V44C65 48 30 56 0 62Z" fill="var(--stripe)"/>
  </svg>
  <svg class="panel__base" viewBox="0 0 100 30" preserveAspectRatio="none">
    <path d="M0 30V2C40 0 70 0 100 2V30Z" fill="var(--orange)"/>
  </svg>
  <div class="panel__content" style="top:172px">
    <ul class="services services--narrow">
      <li>Water and Flood</li><li>Fire and Smoke</li><li>Mold and Biohazard</li><li>Structural Repair</li><li>Asset Protection</li>
    </ul>
  </div>
</section>

<!-- Wide slogan panel -->
<section class="panel" style="left:689px;width:173px">
  <div class="panel__photo" role="img" aria-label="Flooded commercial plaza with trees and office towers"></div>
  <svg class="panel__sky" viewBox="0 0 100 100" preserveAspectRatio="none">
    <path d="M0 0H100V32C65 30 30 34 0 42Z" fill="url(#sky)"/>
    <path d="M0 42C30 34 65 30 100 32V36C65 34 30 38 0 46Z" fill="var(--stripe)"/>
  </svg>
  <svg class="panel__base" viewBox="0 0 100 30" preserveAspectRatio="none">
    <path d="M0 30V0C40 2 70 6 100 8V30Z" fill="var(--orange)"/>
  </svg>
  <div class="panel__content" style="top:96px">
    <div class="brand__name"><span class="brand__primary" style="font-size:28px">CORVANE</span><span class="brand__secondary">RESTORATION SERVICES</span></div>
    <p class="slogan">Exceeding your<br>expectations when<br>you need it most</p>
  </div>
</section>

<!-- Narrow services panel, right -->
<section class="panel" style="left:890px;width:104px">
  <div class="panel__photo" role="img" aria-label="Office towers reflected in floodwater"></div>
  <svg class="panel__sky" viewBox="0 0 100 100" preserveAspectRatio="none">
    <path d="M0 0H100V42C65 34 30 30 0 28Z" fill="url(#sky)"/>
    <path d="M0 28C30 30 65 34 100 42V48C65 40 30 36 0 34Z" fill="var(--stripe)"/>
  </svg>
  <svg class="panel__base" viewBox="0 0 100 30" preserveAspectRatio="none">
    <path d="M0 30V4C40 6 70 6 100 4V30Z" fill="var(--orange)"/>
  </svg>
  <div class="panel__content" style="top:157px">
    <ul class="services services--narrow">
      <li>Water and Flood</li><li>Fire and Smoke</li><li>Mold and Biohazard</li><li>Structural Repair</li><li>Asset Protection</li>
    </ul>
  </div>
</section>

<!-- Services panel, right -->
<section class="panel" style="left:1013px;width:153px">
  <div class="panel__photo" role="img" aria-label="Flooded commercial downtown street with office towers in mist"></div>
  <svg class="panel__sky" viewBox="0 0 100 100" preserveAspectRatio="none">
    <path d="M0 0H100V76C70 50 35 40 0 38Z" fill="url(#sky)"/>
    <path d="M0 38C35 40 70 50 100 76V84C70 58 35 46 0 44Z" fill="var(--stripe)"/>
  </svg>
  <svg class="panel__base" viewBox="0 0 100 30" preserveAspectRatio="none">
    <path d="M0 30V0C35 2 70 8 100 14V30Z" fill="var(--orange)"/>
  </svg>
  <div class="panel__content" style="top:100px">
    <div class="brand__name"><span class="brand__primary" style="font-size:26px">CORVANE</span><span class="brand__secondary">RESTORATION SERVICES</span></div>
    <ul class="services services--wide">
      <li>Water and Flood</li><li>Fire and Smoke</li><li>Mold and Biohazard</li><li>Structural Repair</li><li>Asset Protection</li>
    </ul>
  </div>
</section>
</body>
</html>
```